Business Card for my New Brokerage

Looking to get a business card design for my new Real Estate Brokerage.
I want it with Picture, Phone Number, Email, Website, Office Address
Name and Designation. Please add logo too.

Target Market(s)

Real Estate Investors or Home Buyers

Industry/Entity Type

Real Estate

Contact Information for Business Card

Name, Email, Phone Number, website, email, office address

Colors
EB3D1F
EC4F4E
F09395
F8D3D4
FCEDEE

Requirements
Must have
• Minimalistic, Clean, Modern, Photo
Nice to have
• White and Red Colors

```html
<!DOCTYPE html>
<html lang="en">
<head>
<meta charset="utf-8">
<title>Cedar Row Realty — Business Card</title>
<link rel="stylesheet" href="https://fonts.googleapis.com/css2?family=Montserrat:wght@500;600;800&display=swap">
<style>
  :root {
    --red: #e01f26;
    --gold: #d9b44a;
    --white: #ffffff;
    --ink: #1d1d1f;
    --backdrop: #c4c4c4;
    --photo-light: #f1f3f6;
    --photo-mid: #aebbd0;
    --photo-dark: #2c4466;
  }
  * { box-sizing: border-box; margin: 0; padding: 0; }
  html, body { width: 1200px; height: 788px; overflow: hidden; }
  body {
    background: var(--backdrop);
    font-family: "Montserrat", Arial, sans-serif;
    display: flex;
    align-items: center;
    justify-content: center;
    gap: 40px;
  }
  .card {
    position: relative;
    width: 540px;
    height: 310px;
    border-radius: 22px;
    overflow: hidden;
    box-shadow: 0 14px 30px rgba(0,0,0,0.22);
  }

  /* Front */
  .card-front { background: var(--white); }
  .portrait {
    position: absolute;
    left: 300px; top: 40px;
    width: 215px; height: 200px;
    background: linear-gradient(180deg, var(--photo-light) 0%, var(--photo-mid) 55%, var(--photo-dark) 100%);
    border-radius: 16px 16px 0 0;
  }
  .swoosh { position: absolute; inset: 0; width: 540px; height: 310px; }

  .brand-front {
    position: absolute;
    left: 30px; top: 46px;
    color: var(--red);
    font-weight: 600;
    font-size: 26px;
    line-height: 1;
  }

  .identity {
    position: absolute;
    left: 0; top: 124px;
    padding-left: 38px;
  }
  .identity::before {
    content: "";
    position: absolute;
    left: 0; top: 2px;
    width: 16px; height: 32px;
    background: var(--red);
  }
  .person-name { color: var(--red); font-weight: 800; font-size: 17px; letter-spacing: 0.3px; line-height: 1.2; }
  .person-role { color: var(--ink); font-weight: 500; font-size: 12px; margin-top: 2px; }

  .address {
    position: absolute;
    left: 48px; top: 178px;
    color: var(--ink);
    font-size: 12px;
    font-weight: 500;
    line-height: 1.4;
  }
  .contacts {
    position: absolute;
    left: 36px; top: 222px;
    list-style: none;
    color: var(--ink);
    font-size: 12px;
    font-weight: 500;
  }
  .contacts li { display: flex; align-items: center; gap: 7px; height: 18px; }
  .contacts svg { width: 11px; height: 11px; flex: none; }

  /* Back */
  .card-back {
    background: var(--red);
    display: flex;
    align-items: center;
    justify-content: center;
  }
  .brand-back {
    color: var(--white);
    font-weight: 600;
    font-size: 50px;
    line-height: 1;
  }
</style>
</head>
<body>
  <section class="card card-front">
    <div class="portrait" role="img" aria-label="Portrait photo of the broker in a navy blazer and light blue shirt"></div>
    <svg class="swoosh" viewBox="0 0 540 310" aria-hidden="true">
      <path d="M186 310 C 320 284, 460 206, 530 30 L540 30 L540 310 Z" fill="var(--gold)"/>
      <path d="M198 310 C 330 284, 470 210, 540 44 L540 310 Z" fill="var(--red)"/>
    </svg>

    <div class="brand-front">Cedar Row Realty</div>

    <div class="identity">
      <div class="person-name">DALEN BROOKS</div>
      <div class="person-role">Owner/CEO</div>
    </div>

    <div class="address">
      1450 W Harlow Avenue<br>
      Marsden County 4187
    </div>

    <ul class="contacts">
      <li>
        <svg viewBox="0 0 12 12"><circle cx="6" cy="6" r="6" fill="var(--red)"/><path d="M4 3.2l1 1.2-.6.8a4 4 0 0 0 2.4 2.4l.8-.6 1.2 1-.6.9c-2.6-.2-4.6-2.2-4.9-4.9z" fill="var(--white)"/></svg>
        123-555-01987
      </li>
      <li>
        <svg viewBox="0 0 12 12"><circle cx="6" cy="6" r="6" fill="var(--red)"/><rect x="3" y="4" width="6" height="4" fill="var(--white)"/><path d="M3 4l3 2.2L9 4" fill="none" stroke="var(--red)" stroke-width=".8"/></svg>
        info@cedarrowrealty.com
      </li>
      <li>
        <svg viewBox="0 0 12 12"><circle cx="6" cy="6" r="6" fill="var(--red)"/><circle cx="6" cy="6" r="3" fill="none" stroke="var(--white)" stroke-width=".9"/><path d="M3 6h6M6 3v6" stroke="var(--white)" stroke-width=".8"/></svg>
        www.cedarrowrealty.com
      </li>
    </ul>
  </section>

  <section class="card card-back">
    <div class="brand-back">Cedar Row Realty</div>
  </section>
</body>
</html>
```